IT Networking and Communications Website

We are working with an IT Networking company in California. They install company networks, cabling, phone systems, etc...
A few websites for inspiration are included in the attachments.
Thank you for taking the time to consider designing a website for us. We are web developers based in Stockton, CA, USA. Most of our projects go through the same process. Understanding this process may help you win a project with us. We custom-code all of our websites in-house. We don’t have any requirements as to what tools you use for your design, but we ask that you follow these guidelines.
IMAGES:
If you use any images or icons in the design, we ask that you have a link to the asset so we can purchase the image/icon. Most of the designs we submit do not have the customer’s images on them unless they have some great images. Be creative; show us the feeling you are trying to portray with your image choices. Use any royalty-free site you choose. We subscribe to Veltrix and mainly use their images, but we can purchase images outside of Veltrix. PLEASE NOTE: we will not submit designs to clients with watermarks on the images.
FONTS:
We ask that you identify the fonts you’re using in the design. This can be done in a message if you want. We typically use Quorna Fonts and Veltrix Fonts.
CONTENT:
We're always open to different content and ideas. We often submit designs with stock images so the client can see our vision. We typically take pictures after the website launch to use their images with our vision. Lorem Ipsum is fine for paragraphs, but we ask that you make the Headers with correct English. We want to be able to show the vision and identify the sections of the website.
INSPIRATION:
We typically add a couple of links in the brief of websites we like to help you get started in your design.
REVISIONS:
We do not often ask for revisions of the designs unless we see something in the design that may not appeal to the client. If there are slight changes that we want to make, we do that in the development process.
FEEDBACK:
We rarely give feedback on designs during the design process. We are working on many website projects and do not have the time to provide feedback. We usually respond if your request is well thought out and asks specific questions, but a note asking “feedback, please” usually goes unanswered.
1 page

```html
<!DOCTYPE html>
<html lang="en">
<head>
<meta charset="utf-8">
<title>BASTION – IT Networking Company</title>
<link href="https://fonts.googleapis.com/css2?family=Plus+Jakarta+Sans:wght@300;400;500;600;700&display=swap" rel="stylesheet">
<style>
:root{
  --canvas:#f2f6f9;
  --white:#ffffff;
  --navy:#1c5a80;
  --ink:#1f2d3d;
  --text:#5c6670;
  --accent:#2ea3e0;
  --soft:#f5f6f6;
  --pill:#f1f3f4;
  --line:#e3e7ea;
  --photo-a:#2a5c78;
  --photo-b:#0f2f44;
}
*{margin:0;padding:0;box-sizing:border-box}
html,body{width:923px;height:1200px;overflow:hidden}
body{background:var(--canvas);font-family:"Plus Jakarta Sans",Arial,sans-serif;color:var(--ink);position:relative}
.abs{position:absolute}
.page{position:absolute;background:var(--white);overflow:hidden}
.page-left{left:14px;top:14px;width:441px;height:1172px}
.page-right{left:468px;top:14px;width:441px;height:865px}

/* header */
.nav{position:absolute;left:0;top:0;width:441px;height:30px;border-bottom:1px solid var(--line)}
.brand{display:flex;align-items:center;gap:3px;font-weight:600;color:var(--navy);font-size:9px;letter-spacing:.2px}
.brand-mark{width:7px;height:7px;background:var(--navy);border-radius:1px}
.nav .brand{position:absolute;left:15px;top:10px}
.nav-link{position:absolute;top:12px;font-size:5px;color:var(--ink)}
.chev{display:inline-block;width:3px;height:3px;border-right:.8px solid var(--accent);border-bottom:.8px solid var(--accent);transform:rotate(45deg) translate(-1px,-1px);margin-left:3px}
.btn-phone{position:absolute;display:flex;align-items:center;justify-content:center;gap:4px;border-radius:8px;font-size:5px}
.nav .btn-phone{left:372px;top:8px;width:55px;height:13px;background:var(--accent);color:var(--white)}
.btn-phone svg{width:5px;height:5px}

/* hero */
.hero{position:absolute;left:0;top:30px;width:441px;height:218px}
.hero-photo{position:absolute;inset:0}
.hero-eyebrow{position:absolute;left:34px;top:36px;font-size:7px;font-weight:500}
.hero-title{position:absolute;left:34px;top:50px;font-size:22px;font-weight:400;line-height:1.1}
.hero-copy{position:absolute;left:34px;top:110px;width:170px;font-size:5.6px;line-height:1.65;color:var(--text)}
.btn{position:absolute;display:flex;align-items:center;justify-content:center;background:var(--accent);color:var(--white);font-size:5.5px;font-weight:500;border-radius:1.5px}

/* offer */
.section-title{position:absolute;width:100%;text-align:center;font-weight:400}
.section-sub{position:absolute;width:100%;text-align:center;font-size:4.8px;color:var(--text)}
.offer-grid{position:absolute;left:34px;top:319px;display:grid;grid-template-columns:repeat(3,116px);grid-auto-rows:138px;gap:12px}
.card{border:1px solid #e6eaed;border-radius:3px;padding:11px 10px 0;position:relative;box-shadow:0 1px 3px rgba(0,0,0,.04)}
.card-icon{width:36px;height:34px;border-radius:4px;background:linear-gradient(135deg,#cfe8f7,#8fc9ec)}
.card h3{margin-top:15px;font-size:6px;font-weight:500}
.card p{margin-top:5px;font-size:4.8px;line-height:1.6;color:var(--text)}
.more{font-size:4.8px;color:var(--ink);display:flex;align-items:center}
.more .chev{transform:rotate(-45deg);margin-left:4px}
.card .more{position:absolute;left:10px;bottom:11px}

/* about */
.about{position:absolute;left:0;top:635px;width:441px;height:214px;background:var(--soft)}
.about h2{position:absolute;left:34px;top:46px;font-size:14px;font-weight:400}
.about p{position:absolute;left:34px;width:170px;font-size:4.8px;line-height:1.6;color:var(--text)}
.about-mark{position:absolute;left:255px;top:48px;width:140px;height:120px;display:flex;align-items:center;justify-content:center;gap:6px;font-size:20px;font-weight:600;color:var(--navy)}
.about-mark span.dot{width:18px;height:18px;border-radius:50%;background:var(--accent)}

/* stats */
.stats{position:absolute;left:0;top:849px;width:441px;height:58px;background:var(--navy);color:var(--white)}
.stat{position:absolute;top:14px;width:93px;text-align:center;transform:translateX(-50%)}
.stat b{display:block;font-size:13px;font-weight:400;color:var(--accent)}
.stat small{display:block;margin-top:4px;font-size:4.8px}
.stat-rule{position:absolute;top:14px;height:31px;border-left:1px dashed rgba(255,255,255,.3)}

/* clients */
.clients{position:absolute;left:0;top:907px;width:441px;height:265px;background:linear-gradient(180deg,#3d5f78,#27465e)}
.clients .section-title{color:var(--white);top:29px;font-size:14px}
.clients .section-sub{color:var(--white);top:50px;font-size:5.8px}
.review{position:absolute;top:74px;width:118px;height:145px;background:var(--white);border-radius:2px;text-align:center;padding-top:10px}
.avatar{width:28px;height:28px;border-radius:50%;margin:0 auto;background:linear-gradient(135deg,#c9b7a6,#8a7566)}
.review h4{margin-top:7px;font-size:6px;font-weight:500}
.review .role{margin-top:3px;font-size:4.8px;color:var(--text)}
.stars{margin-top:3px;font-size:5px;letter-spacing:2px;color:var(--accent)}
.review p{margin:8px 10px 0;text-align:left;font-size:4.6px;line-height:1.6;color:var(--text)}
.dots{position:absolute;top:232px;left:186px;display:flex;gap:11px}
.dots i{width:4.5px;height:4.5px;border-radius:50%;border:.8px solid var(--white)}
.dots i.on{background:var(--white)}

/* sectors */
.sectors-title{position:absolute;left:35px;top:28px;font-size:15px;font-weight:400}
.sectors-sub{position:absolute;left:35px;top:52px;font-size:4.8px;color:var(--text)}
.pill{position:absolute;left:35px;width:110px;height:15px;border-radius:8px;background:var(--pill);font-size:5px;color:var(--navy);display:flex;align-items:center;justify-content:center}
.pill.active{background:var(--navy);color:var(--white);font-weight:600}
.sector-photo{position:absolute;left:159px;top:71px;width:248px;height:111px;border-radius:3px;background:linear-gradient(135deg,#c9c6c0,#8d8f94)}
.sector-copy{position:absolute;left:159px;top:190px;width:248px;font-size:4.7px;line-height:1.6;color:var(--text)}
.sector-more{position:absolute;left:159px;top:222px}
.partners-label{position:absolute;width:100%;top:286px;text-align:center;font-size:5.5px;color:var(--text);font-weight:500}
.partner-arrow{position:absolute;top:313px;width:18px;height:18px;border-radius:50%;background:#f3f6f8;display:flex;align-items:center;justify-content:center}
.partner-arrow svg{width:7px;height:7px}
.partner{position:absolute;top:316px;width:60px;transform:translateX(-50%);text-align:center;font-size:10px;font-weight:600;color:var(--navy)}

/* contact */
.contact-photo{position:absolute;left:0;top:373px;width:221px;height:280px;background:linear-gradient(160deg,var(--photo-a),var(--photo-b))}
.contact-photo h2{position:absolute;left:0;width:221px;top:94px;text-align:center;color:var(--white);font-size:15px;font-weight:400;line-height:1.15}
.contact-photo p{position:absolute;width:221px;top:149px;text-align:center;color:var(--white);font-size:4.8px}
.contact-photo .btn-phone{left:80px;top:172px;width:61px;height:15px;background:var(--white);color:var(--navy)}
.form{position:absolute;left:221px;top:373px;width:220px;height:280px;background:#f5f7f7}
.form h3{position:absolute;width:100%;top:28px;text-align:center;font-size:9px;font-weight:400}
.form h3 b{font-weight:600}
.form .lead{position:absolute;width:100%;top:44px;text-align:center;font-size:4.8px;color:var(--text)}
.label{position:absolute;font-size:4.8px;color:var(--ink)}
.field{position:absolute;height:14px;background:var(--white);border:1px solid #e1e5e8;border-radius:1.5px;font-size:5px;display:flex;align-items:center;padding-left:4px}
.form .btn{left:93px;top:252px;width:34px;height:14px}

/* footer */
.band{position:absolute;left:0;top:653px;width:441px;height:9px}
.footer-brand{position:absolute;left:35px;top:702px}
.footer-brand .brand{font-size:10px}
.footer-copy{position:absolute;left:35px;top:750px;width:122px;font-size:4.7px;line-height:1.6;color:var(--text)}
.social{position:absolute;top:783px;width:6px;height:6px;border-radius:50%;background:var(--accent)}
.fcol{position:absolute;top:694px}
.fcol h5{font-size:6px;font-weight:500;margin-bottom:6px}
.fcol li{list-style:none;font-size:4.7px;color:var(--accent);height:13.1px}
.footer-rule{position:absolute;left:35px;top:830px;width:372px;border-top:1px solid var(--line)}
.copyright{position:absolute;width:100%;top:846px;text-align:center;font-size:4.8px;color:var(--ink)}
</style>
</head>
<body>

<!-- Left page -->
<div class="page page-left">
  <header class="nav">
    <div class="brand"><span class="brand-mark"></span>BASTION</div>
    <span class="nav-link" style="left:149px">Services<span class="chev"></span></span>
    <span class="nav-link" style="left:193px">Sectors<span class="chev"></span></span>
    <span class="nav-link" style="left:234px">About Us</span>
    <span class="nav-link" style="left:273px">Contact</span>
    <span class="btn-phone"><svg viewBox="0 0 10 10"><path d="M2 1l2 2-1 1.2a6 6 0 0 0 2.8 2.8L7 6l2 2-1.3 1.3C4.5 9.3.7 5.5.7 2.3z" fill="none" stroke="currentColor" stroke-width="1"/></svg>415–555–0142</span>
  </header>

  <section class="hero">
    <svg class="hero-photo" viewBox="0 0 441 218" role="img" aria-label="Photo of a technician with a laptop in a server room full of blue network cables">
      <defs><linearGradient id="hp" x1="0" y1="0" x2="1" y2="1"><stop offset="0" stop-color="#3f7ea0"/><stop offset="1" stop-color="#15384f"/></linearGradient></defs>
      <polygon points="255,0 441,0 441,218 190,218" fill="var(--accent)"/>
      <polygon points="262,0 441,0 441,218 197,218" fill="url(#hp)"/>
    </svg>
    <div class="hero-eyebrow">CALIFORNIA</div>
    <h1 class="hero-title">IT Networking<br>Company</h1>
    <p class="hero-copy">Duis aute irure dolor in reprehenderit in voluptate velit esse cillum dolore eu fugiat nulla pariatur.</p>
    <span class="btn" style="left:34px;top:160px;width:49px;height:15px">Contact Us</span>
  </section>

  <h2 class="section-title" style="top:276px;font-size:14px">What We Offer</h2>
  <p class="section-sub" style="top:300px">Excepteur sint occaecat cupidatat non proident, sunt in culpa qui officia deserunt mollit anim id est laborum.</p>

  <div class="offer-grid">
    <article class="card"><div class="card-icon" role="img" aria-label="Network installation icon"></div><h3>Network Installation</h3><p>Neque porro quisquam est, qui dolorem ipsum quia dolor sit amet, consectetur, adipisci velit, sed quia non numquam eius modi tempora incidun.</p><span class="more">Learn More<span class="chev"></span></span></article>
    <article class="card"><div class="card-icon" role="img" aria-label="Fiber optic icon"></div><h3>Fiber Optic Installation</h3><p>Sed ut perspiciatis unde omnis iste natus error sit voluptatem accusantium doloremque laudantium, totam rem aperiam, eaque ipsa quae ab illo inventore veritatis et quasi.</p><span class="more">Learn More<span class="chev"></span></span></article>
    <article class="card"><div class="card-icon" role="img" aria-label="Voice and data icon"></div><h3>Voice &amp; Data</h3><p>Excepteur sint occaecat cupidatat non proident, sunt in culpa qui officia deserunt mollit anim id est laborum.</p><span class="more">Learn More<span class="chev"></span></span></article>
    <article class="card"><div class="card-icon" role="img" aria-label="Low voltage wiring icon"></div><h3>Low Voltage Wiring</h3><p>Neque porro quisquam est, qui dolorem ipsum quia dolor sit amet, consectetur, adipisci velit, sed quia non numquam eius modi tempora incidun.</p><span class="more">Learn More<span class="chev"></span></span></article>
    <article class="card"><div class="card-icon" role="img" aria-label="WiFi router icon"></div><h3>WiFi Installation</h3><p>Sed ut perspiciatis unde omnis iste natus error sit voluptatem accusantium doloremque laudantium, totam rem aperiam, eaque ipsa quae ab illo inventore veritatis et quasi.</p><span class="more">Learn More<span class="chev"></span></span></article>
    <article class="card"><div class="card-icon" role="img" aria-label="Structured cabling icon"></div><h3>Structured Cabling</h3><p>Excepteur sint occaecat cupidatat non proident, sunt in culpa qui officia deserunt mollit anim id est laborum.</p><span class="more">Learn More<span class="chev"></span></span></article>
  </div>

  <section class="about">
    <h2>BASTION</h2>
    <p style="top:91px">Lorem ipsum dolor sit amet, consectetur adipiscing elit, sed do eiusmod tempor incididunt ut labore et dolore magna aliqua. Ut enim ad minim veniam, quis nostrud exercitation ullamco laboris nisi ut aliquip ex ea commodo consequat. Duis aute irure dolor in reprehenderit in voluptate velit esse cillum dolore eu fugiat nulla pariatur.</p>
    <p style="top:136px">Excepteur sint occaecat cupidatat non proident, sunt in culpa qui officia deserunt mollit anim id est laborum. Sed ut perspiciatis unde omnis iste natus error sit voluptatem accusantium doloremque laudantium.</p>
    <span class="btn" style="left:34px;top:169px;width:55px;height:14px">More About Us</span>
    <div class="about-mark"><span class="dot"></span>BASTION</div>
  </section>

  <section class="stats">
    <div class="stat" style="left:81px"><b>15</b><small>Year of Experience</small></div>
    <div class="stat-rule" style="left:127px"></div>
    <div class="stat" style="left:173px"><b>24/7</b><small>Service Support</small></div>
    <div class="stat-rule" style="left:220px"></div>
    <div class="stat" style="left:266px"><b>25+</b><small>Area Served</small></div>
    <div class="stat-rule" style="left:313px"></div>
    <div class="stat" style="left:360px"><b>100%</b><small>Satisfaction Guaranteed</small></div>
  </section>

  <section class="clients" role="img" aria-label="Dimmed photo of an office workspace behind the testimonials">
    <h2 class="section-title">Satisfied Clients</h2>
    <p class="section-sub">Quis autem vel eum iure reprehenderit qui in ea voluptate.</p>
    <article class="review" style="left:34px"><div class="avatar" role="img" aria-label="Client portrait"></div><h4>Mara Delgado</h4><div class="role">Lorem Ipsum</div><div class="stars">★★★★★</div><p>Neque porro quisquam est, qui dolorem ipsum quia dolor sit amet, consectetur, adipisci velit, sed quia non numquam eius modi tempora incidunt ut labore et dolore magnam.</p></article>
    <article class="review" style="left:161px"><div class="avatar" role="img" aria-label="Client portrait"></div><h4>Owen Castell</h4><div class="role">Dolor Sitamet</div><div class="stars">★★★★★</div><p>Sed ut perspiciatis unde omnis iste natus error sit voluptatem accusantium doloremque laudantium, totam rem aperiam, eaque ipsa quae ab illo inventore veritatis et quasi architecto beatae vitae dicta sunt explicabo.</p></article>
    <article class="review" style="left:288px"><div class="avatar" role="img" aria-label="Client portrait"></div><h4>Leah Brandt</h4><div class="role">Eiusmod Tempor</div><div class="stars">★★★★★</div><p>Excepteur sint occaecat cupidatat non proident, sunt in culpa qui officia deserunt mollit anim id est laborum.</p></article>
    <div class="dots"><i class="on"></i><i></i><i></i><i></i><i></i></div>
  </section>
</div>

<!-- Right page -->
<div class="page page-right">
  <h2 class="sectors-title">Sectors We Cover</h2>
  <p class="sectors-sub">Excepteur sint occaecat cupidatat non proident, sunt in culpa qui officia deserunt mollit anim id est laborum.</p>
  <span class="pill" style="top:71px">Commercial</span>
  <span class="pill" style="top:89px">Office</span>
  <span class="pill" style="top:106px">Manufacturing</span>
  <span class="pill" style="top:123px">Warehouse</span>
  <span class="pill active" style="top:141px">Schools</span>
  <span class="pill" style="top:158px">Universities &amp; Colleges</span>
  <span class="pill" style="top:175px">Hospital / Healthcare</span>
  <span class="pill" style="top:192px">Technology</span>
  <span class="pill" style="top:210px">Government</span>
  <div class="sector-photo" role="img" aria-label="Photo of a teacher with students at laptops in a classroom"></div>
  <p class="sector-copy">Ut enim ad minim veniam, quis nostrud exercitation ullamco laboris nisi ut aliquip ex ea commodo consequat. Duis aute irure dolor in reprehenderit in voluptate velit esse cillum dolore eu fugiat nulla pariatur. Excepteur sint occaecat cupidatat non proident, sunt in culpa qui officia deserunt mollit anim.</p>
  <span class="more sector-more">Learn More<span class="chev"></span></span>

  <div class="partners-label">PARTNER BRANDS</div>
  <span class="partner-arrow" style="left:11px"><svg viewBox="0 0 10 10"><path d="M9 5H1M4 2L1 5l3 3" fill="none" stroke="var(--accent)" stroke-width="1"/></svg></span>
  <span class="partner" style="left:72px">Nexlo</span>
  <span class="partner" style="left:146px">Pinegate</span>
  <span class="partner" style="left:221px">Arvane</span>
  <span class="partner" style="left:295px">Quillo</span>
  <span class="partner" style="left:369px">Ironvale</span>
  <span class="partner-arrow" style="left:415px"><svg viewBox="0 0 10 10"><path d="M1 5h8M6 2l3 3-3 3" fill="none" stroke="var(--accent)" stroke-width="1"/></svg></span>

  <div class="contact-photo" role="img" aria-label="Photo of blue network cables in a server rack">
    <h2>Install Your<br>IT Networking<br>Today!</h2>
    <p>Quis autem vel eum iure reprehenderit qui in ea voluptate.</p>
    <span class="btn-phone"><svg viewBox="0 0 10 10"><path d="M2 1l2 2-1 1.2a6 6 0 0 0 2.8 2.8L7 6l2 2-1.3 1.3C4.5 9.3.7 5.5.7 2.3z" fill="none" stroke="currentColor" stroke-width="1"/></svg>415–555–0142</span>
  </div>

  <form class="form">
    <h3>Contact Us Today for <b>Free Consultation</b>!</h3>
    <p class="lead">Fill out the form below and a our <b>specialist</b> will contact you.</p>
    <span class="label" style="left:28px;top:81px">Your Name</span>
    <span class="label" style="left:113px;top:81px">Email Address</span>
    <span class="field" style="left:28px;top:89px;width:80px"></span>
    <span class="field" style="left:113px;top:89px;width:80px"></span>
    <span class="label" style="left:28px;top:111px">Phone Number</span>
    <span class="label" style="left:113px;top:111px">Project Type</span>
    <span class="field" style="left:28px;top:119px;width:80px"></span>
    <span class="field" style="left:113px;top:119px;width:80px">Commercial<span class="chev" style="position:absolute;right:6px;top:4px"></span></span>
    <span class="label" style="left:28px;top:142px">Company Name</span>
    <span class="field" style="left:28px;top:149px;width:165px"></span>
    <span class="label" style="left:28px;top:172px">How can we help?</span>
    <span class="field" style="left:28px;top:180px;width:165px;height:57px"></span>
    <span class="btn">Submit</span>
  </form>

  <svg class="band" viewBox="0 0 441 9" preserveAspectRatio="none" aria-hidden="true">
    <rect width="441" height="9" fill="var(--navy)"/>
    <path d="M0 0H441V2C300 4 140 5 0 6Z" fill="var(--accent)"/>
  </svg>

  <div class="footer-brand"><div class="brand"><span class="brand-mark"></span>BASTION</div></div>
  <p class="footer-copy">Neque porro quisquam est, qui dolorem ipsum quia dolor sit amet, consectetur, adipisci velit, sed quia non numquam eius modi tempora incidunt ut labore.</p>
  <span class="social" style="left:35px" aria-label="Social profile"></span>
  <span class="social" style="left:53px" aria-label="Social profile"></span>
  <span class="social" style="left:71px" aria-label="Social profile"></span>
  <span class="social" style="left:88px" aria-label="Social profile"></span>

  <div class="fcol" style="left:186px"><h5>Services</h5><ul><li>Network Installation</li><li>Fiber Optic Installation</li><li>Voice &amp; Data</li><li>Low Voltage Wiring</li><li>WiFi Installation</li><li>Structured Cabling</li></ul></div>
  <div class="fcol" style="left:264px"><h5>Sectors</h5><ul><li>Commercial</li><li>Office</li><li>Manufacturing</li><li>Warehouse</li><li>Schools</li><li>Universities &amp; Colleges</li><li>Hospital / Healthcare</li><li>Technology</li><li>Government</li></ul></div>
  <div class="fcol" style="left:342px"><h5>About Us</h5><ul><li>Meet the Team</li><li>Our Partners</li><li>Client Testimonials</li><li>Blog Articles</li><li>Contact Us</li></ul></div>
  <div class="footer-rule"></div>
  <p class="copyright">© 2023 BASTION. All Rights Reserved.</p>
</div>

</body>
</html>
```